Velmira Body Oil Label for 4 -8 oz bottles

We are selling 4 and 8 oz body oils and need a label to put on our bottles. I'm not sure if we want a label for the front and also the back of the bottle or just one label in the front. You can give me examples of each way. Attached is our logo on a blue background but the background will change colors depending on the scent as specified in the design description. Our bottle will be either clear or white with a pump spray type lid as shown in the attached example. Attached are also our design criteria which is needed for the labels.
Updates

We have decided to use the disc top cap and not the pump spray cap. If you are able to, please show us the design on the 4 oz bottle with the disc top cap. Thanks

Target Market(s)

women

Industry/Entity Type

skincare, cosmetics

Font styles to use
Serif
Sans Serif

Requirements
Must have
• stylish name for each scented oil which contrasts the font in the logo. Also must have darker colors since the logo colors are lighter.
Nice to have
• Border around the labels, maybe one solid color or maybe two complimenting colors which go well with the fragrnace name
Should not have
• background colors that match the logo colors

```html
<!DOCTYPE html>
<html lang="en">
<head>
<meta charset="utf-8">
<title>Velmira Body Oil Label</title>
<link rel="stylesheet" href="https://fonts.googleapis.com/css2?family=Roboto:ital,wght@0,400;0,500;1,400;1,500&family=Caveat:wght@500&display=swap">
<style>
  :root {
    --band: #9d6459;
    --band-line: #8e564c;
    --blush: #f9d6ce;
    --ink: #9a6157;
    --ink-soft: #8a5c55;
    --paper: #ffffff;
    --white-text: #ffffff;
  }
  * { margin: 0; padding: 0; box-sizing: border-box; }
  html, body {
    width: 1200px; height: 900px; overflow: hidden;
    background: var(--paper);
    font-family: "Roboto", Arial, sans-serif;
  }
  .label {
    position: absolute;
    left: 52px; top: 25px;
    width: 644px; height: 500px;
    transform: scale(1.7);
    transform-origin: top left;
    border-radius: 16px;
    overflow: hidden;
    background: var(--blush);
  }
  .label__band {
    position: absolute; left: 0; top: 0;
    width: 100%; height: 178px;
    background: var(--band);
  }
  .label__rule {
    position: absolute; left: 0; top: 183px;
    width: 100%; height: 3px;
    background: var(--band-line);
  }
  .brand {
    position: absolute; left: 240px; top: 74px;
    width: 164px; text-align: center;
    display: flex; align-items: center; justify-content: center; gap: 7px;
    color: var(--white-text);
    font-size: 28px; font-weight: 400; letter-spacing: 0.5px;
  }
  .brand__dot {
    width: 9px; height: 9px; border-radius: 50%;
    background: var(--white-text);
  }
  .panel {
    position: absolute; left: 472px; width: 150px;
    text-align: center;
    font-size: 8px; line-height: 10.2px;
  }
  .panel__title {
    font-style: italic; font-weight: 500;
    font-size: 10px; margin-bottom: 6px;
  }
  .panel--ingredients { top: 45px; color: var(--white-text); }
  .panel--directions { top: 206px; color: var(--ink-soft); }
  .panel--warnings { top: 264px; color: var(--ink-soft); }
  .panel--distributor { top: 423px; color: var(--ink-soft); }
  .scent-name {
    position: absolute; left: 214px; top: 200px;
    width: 220px; text-align: center;
    font-family: "Caveat", cursive;
    font-weight: 500; font-size: 34px;
    color: var(--ink);
  }
  .claims__rule {
    position: absolute; left: 280px; top: 392px;
    width: 84px; height: 1px; background: var(--ink-soft);
  }
  .claims {
    position: absolute; left: 242px; top: 403px;
    width: 160px; text-align: center;
    font-style: italic; font-size: 9px; line-height: 12.5px;
    color: var(--ink-soft);
  }
  .net-weight {
    position: absolute; left: 232px; top: 466px;
    width: 180px; text-align: center;
    font-size: 9px; color: var(--ink-soft);
  }
</style>
</head>
<body>
  <section class="label" aria-label="Velmira body oil bottle label">
    <div class="label__band"></div>
    <div class="label__rule"></div>

    <div class="brand"><span class="brand__dot"></span>Velmira</div>

    <div class="panel panel--ingredients">
      <p class="panel__title">Ingredients :</p>
      <p>Cocos Nucifera (Coconut) Oil, Prunus Amygdalus Dulcis (Almond) Oil, Vitis Vinifera (Grapeseed) Oil, Sesamum Indicum (Sesame) Seed Oil, Simmondsia Chinensis (Jojoba) Oil, Tocopheryl Acetate (Vitamin E). Essential oils, and fragrances.</p>
    </div>

    <h1 class="scent-name">Berry Bloom</h1>

    <div class="panel panel--directions">
      <p class="panel__title">Directions :</p>
      <p>Apply a small amount to skin and massage until absorbed. Use daily for best results.</p>
    </div>

    <div class="panel panel--warnings">
      <p class="panel__title">Warnings :</p>
      <p>For external use only.<br>Avoid contact with eyes.<br>Discontinue use if irritation occurs.<br>Keep out of reach of children.<br>Contains nut oils — use with caution if you have nut allergies.</p>
    </div>

    <div class="claims__rule"></div>
    <p class="claims">Non-Greasy<br>With Vitamin E<br>Ultra Moisturizing</p>

    <p class="net-weight">Net Wt. 4 fl. oz. (118 mL)</p>

    <div class="panel panel--distributor">
      <p class="panel__title">Distributed by</p>
      <p>Velmira<br>482 Alder Crest Lane<br>Fort Collins, CO 80524<br>Made in USA</p>
    </div>
  </section>
</body>
</html>
```